Commercial Real Estate

We need a business card design for a new commercial real estate business that specializes in apartment building brokerage. Not individual units but the entire complex. We find and represent the owners existing buildings and well as new buyers for those buildings. The design should convey trust, integrity, knowledge and growth. It should be easily read.

Target Market(s)

40 to 65 years old

Industry/Entity Type

Real Estate

```html
<!DOCTYPE html>
<html lang="en">
<head>
<meta charset="utf-8">
<title>Larchmont Property – Business Card</title>
<link rel="stylesheet" href="https://fonts.googleapis.com/css2?family=Open+Sans:ital,wght@0,400;0,700;1,400;1,700&display=swap">
<style>
  :root {
    --backdrop: #e4e6e6;
    --card-white: #ffffff;
    --slate: #5a6b69;
    --teal: #6cc8c8;
    --brand-ink: #3f4c4b;
    --text-light: #ffffff;
  }
  html, body {
    margin: 0;
    padding: 0;
    width: 1200px;
    height: 901px;
    overflow: hidden;
    background: var(--backdrop);
    font-family: "Open Sans", sans-serif;
  }
  .card {
    position: absolute;
    left: 100px;
    top: 165px;
    width: 1000px;
    height: 571px;
    border-radius: 60px;
    overflow: hidden;
    background: var(--card-white);
    box-shadow: 0 10px 30px rgba(0,0,0,0.18);
  }
  .card-waves {
    position: absolute;
    inset: 0;
    width: 100%;
    height: 100%;
  }
  .brand {
    position: absolute;
    left: 580px;
    top: 262px;
    display: flex;
    align-items: center;
    gap: 12px;
    white-space: nowrap;
    color: var(--brand-ink);
    font-weight: 700;
    font-size: 28px;
    letter-spacing: 1px;
  }
  .brand-mark {
    width: 16px;
    height: 16px;
    background: var(--teal);
  }
  .contact-list {
    position: absolute;
    left: 70px;
    top: 272px;
    margin: 0;
    padding: 0;
    list-style: none;
    color: var(--text-light);
    font-size: 26px;
    line-height: 42px;
  }
  .contact-list li {
    display: flex;
    align-items: center;
    gap: 12px;
  }
  .contact-icon {
    width: 22px;
    height: 22px;
    flex: none;
  }
  .holder {
    position: absolute;
    right: 80px;
    bottom: 40px;
    text-align: right;
    color: var(--text-light);
  }
  .holder-name {
    font-weight: 700;
    font-style: italic;
    font-size: 30px;
    line-height: 42px;
  }
  .holder-role {
    font-style: italic;
    font-size: 28px;
    line-height: 40px;
  }
</style>
</head>
<body>
  <div class="card">
    <svg class="card-waves" viewBox="0 0 1000 571" preserveAspectRatio="none" aria-hidden="true">
      <path fill="var(--teal)" d="M0,120 C240,210 560,400 1000,345 L1000,571 L0,571 Z"/>
      <path fill="var(--card-white)" d="M0,128 C240,222 560,414 1000,368 L1000,571 L0,571 Z"/>
      <path fill="var(--slate)" d="M0,134 C240,232 560,432 1000,384 L1000,571 L0,571 Z"/>
    </svg>

    <div class="brand">
      <span class="brand-mark"></span>
      <span class="brand-name">LARCHMONT PROPERTY</span>
    </div>

    <ul class="contact-list">
      <li>
        <svg class="contact-icon" viewBox="0 0 24 24" aria-hidden="true"><path fill="#fff" d="M6.6 10.8a15 15 0 0 0 6.6 6.6l2.2-2.2a1 1 0 0 1 1-.25 11.4 11.4 0 0 0 3.6.57 1 1 0 0 1 1 1V20a1 1 0 0 1-1 1A17 17 0 0 1 3 4a1 1 0 0 1 1-1h3.5a1 1 0 0 1 1 1c0 1.25.2 2.45.57 3.57a1 1 0 0 1-.25 1z"/></svg>
        012 555 0147
      </li>
      <li>
        <svg class="contact-icon" viewBox="0 0 24 24" aria-hidden="true"><rect x="3" y="8" width="18" height="12" rx="1" fill="#fff"/><rect x="7" y="3" width="10" height="6" fill="#fff"/><rect x="6" y="12" width="12" height="2" fill="var(--slate)"/></svg>
        012 555 0147
      </li>
      <li>
        <svg class="contact-icon" viewBox="0 0 24 24" aria-hidden="true"><rect x="2" y="5" width="20" height="14" fill="#fff"/><path d="M2 5l10 8 10-8" fill="none" stroke="var(--slate)" stroke-width="1.6"/></svg>
        alden@larchmont.com
      </li>
      <li>071.12th floor,Harbor Lane Road KRD</li>
    </ul>

    <div class="holder">
      <div class="holder-name">Alden Marsh-Cole</div>
      <div class="holder-role">Consultant</div>
    </div>
  </div>
</body>
</html>
```